Verpackungskonzept für Nusskerne, Nussöl, Nussmus
Zielgruppe
Unser Unternehmen stellt verschiedenste Produkte aus Nüssen her.
Unsere Vertriebskanäle sind der gehobene Einzelhandel, sowie direkter Onlinevertrieb.
Unsere Zielgruppe sind umweltbewusste Konsumenten die Wert auf Natürlichkeit,
Nachhaltigkeit und Persönlichkeit/Herzlichkeit legen.
Aufgabenstellung
Für unser Rohwarensortiment (Nusskerne, Nussöl, Nussmus) suchen wir ein Verpackungskonzept und streben eine langfristige Dienstleisterbeziehung (Folgeaufträge) an.
Um Ihnen möglichst wenig unnötige Arbeit zu verursachen, erwarten wir in einem ersten Schritt grobe Konzepte, die im weiteren Verlauf im Detail ausgearbeitet werden.
Ihre Entwürfe sollten folgende Vorgaben erfüllen:
- Berücksichtigen Sie zwei verschiedene Nusssorten als Referenz (Macadamia und Walnuss)
- Berücksichtigen Sie eine visuell einfache Unterscheidung der Nusssorten
- Erstellen Sie bitte Konzepte für
- Öl (Glasflasche 100ml siehe Anhang)
- Nussmus (Glas 250g siehe Anhang)
- Nusskerne (freie Verpackungswahl)
- Berücksichtigen Sie unser Logo (Anhang)
Der Textinhalt ist für die Konzeptausarbeitung nicht relevant.
Bei Rückfragen gerne und jeder Zeit melden.
Herzlichen Dank für Ihre kreativen Vorschläge!

```html
<!DOCTYPE html>
<html lang="de">
<head>
<meta charset="utf-8">
<title>Kernhof – Verpackungskonzept Nusskerne, Nussöl, Nussmus</title>
<link rel="stylesheet" href="https://fonts.googleapis.com/css2?family=Cinzel:wght@500&family=Playfair+Display:wght@900&family=Cormorant+Garamond:ital,wght@1,500&family=Open+Sans:wght@400&display=swap">
<style>
  :root {
    --page: #ffffff;
    --kraft: #d8c4a0;
    --kraft-dark: #c9b28a;
    --ink: #2f2a22;
    --brand-green: #3d5a2a;
    --lid-gold: #8c6b1c;
    --paranuss: #a45a4b;
    --cashew: #9cc63b;
    --note: #222222;
  }
  * { box-sizing: border-box; margin: 0; padding: 0; }
  html, body { width: 848px; height: 1200px; overflow: hidden; background: var(--page); }
  .canvas { position: relative; width: 848px; height: 1200px; font-family: "Open Sans", sans-serif; color: var(--ink); }

  .line-paranuss { --accent: var(--paranuss); --nut-a: #c98f62; --nut-b: #6b3a22; }
  .line-cashew { --accent: var(--cashew); --nut-a: #f1e3c2; --nut-b: #c9ad7c; }

  .brand { font-family: "Cinzel", serif; font-weight: 500; color: var(--brand-green); letter-spacing: 2px; text-transform: uppercase; display: flex; align-items: center; justify-content: center; gap: 5px; }
  .brand-dot { width: 8px; height: 8px; border-radius: 50%; background: var(--brand-green); }
  .product-name { font-family: "Playfair Display", serif; font-weight: 900; text-transform: uppercase; color: var(--ink); line-height: 1; }
  .product-type { font-size: 8px; letter-spacing: 2px; text-transform: uppercase; border-top: 1px solid var(--ink); padding-top: 2px; display: inline-block; }
  .weight { font-family: "Cormorant Garamond", serif; font-style: italic; font-weight: 500; color: var(--ink); }
  .nut-visual { background: radial-gradient(ellipse at 40% 40%, var(--nut-a), var(--nut-b)); border-radius: 40%; }

  /* Deckeletikett */
  .lid { position: absolute; left: 98px; width: 248px; height: 248px; border-radius: 50%; background: var(--lid-gold); padding: 14px; }
  .lid-ring { width: 100%; height: 100%; border-radius: 50%; background: var(--accent); padding: 10px; }
  .lid-face { width: 100%; height: 100%; border-radius: 50%; background: var(--kraft); display: flex; flex-direction: column; align-items: center; justify-content: center; text-align: center; }
  .lid .brand { font-size: 13px; }
  .lid .nut-visual { width: 98px; height: 62px; margin: 8px 0 6px; }
  .lid .product-name { font-size: 19px; }

  /* Glasetikett Mus */
  .jar-label { position: absolute; left: 120px; width: 212px; height: 176px; background: var(--kraft); display: flex; }
  .jar-main { flex: 1; position: relative; display: flex; flex-direction: column; align-items: center; padding-top: 14px; }
  .jar-main .brand { font-size: 12px; }
  .jar-main .nut-visual { width: 118px; height: 70px; margin-top: 12px; }
  .jar-main .weight { position: absolute; left: 10px; bottom: 6px; font-size: 17px; }
  .vertical-band { background: var(--accent); display: flex; align-items: center; justify-content: center; gap: 4px; }
  .vertical-band .stack { writing-mode: vertical-rl; transform: rotate(180deg); display: flex; align-items: center; gap: 4px; }
  .jar-label .vertical-band { width: 50px; }
  .jar-label .product-name { font-size: 26px; }

  /* Flaschenetikett Öl */
  .oil-label { position: absolute; left: 350px; width: 118px; height: 340px; background: #1b1b1b; border-radius: 10px; padding: 22px 6px 10px; display: flex; flex-direction: column; align-items: center; }
  .oil-label > .brand { color: var(--kraft); font-size: 14px; margin-bottom: 16px; }
  .oil-paper { width: 100%; flex: 1; background: var(--kraft); display: flex; flex-direction: column; align-items: center; padding-top: 14px; position: relative; }
  .oil-disc { width: 78px; height: 78px; border-radius: 50%; background: var(--accent); display: flex; align-items: flex-end; justify-content: center; }
  .oil-disc .nut-visual { width: 70px; height: 38px; margin-bottom: -8px; }
  .oil-paper .product-name { font-size: 18px; margin-top: 18px; }
  .oil-paper .weight { position: absolute; right: 8px; bottom: 10px; font-size: 15px; }

  /* Beutel Kerne */
  .bag { position: absolute; left: 516px; width: 234px; height: 502px; background: var(--kraft-dark); }
  .bag-window { position: absolute; left: 14px; top: 120px; width: 118px; height: 230px; border-radius: 14px; }
  .bag .vertical-band { position: absolute; right: 22px; top: 0; width: 54px; height: 400px; }
  .bag .product-name { font-size: 30px; }
  .bag .brand { position: absolute; left: 30px; bottom: 34px; font-size: 16px; }
  .bag .weight { position: absolute; right: 12px; bottom: 28px; font-size: 18px; }

  /* Materialhinweise */
  .note { position: absolute; font-size: 12px; color: var(--note); line-height: 1.25; }
  .note-arrow { position: absolute; width: 1px; background: var(--note); }
  .note-arrow::after { content: ""; position: absolute; left: -4px; bottom: -1px; border-left: 4.5px solid transparent; border-right: 4.5px solid transparent; border-top: 7px solid var(--note); }
</style>
</head>
<body>
<main class="canvas">

  <p class="note" style="left:480px; top:34px;">Naturkarton<br>dunkel</p>
  <span class="note-arrow" style="left:539px; top:76px; height:30px;"></span>
  <p class="note" style="left:660px; top:28px;">Aufkleber<br>gestrichenes Papier</p>
  <span class="note-arrow" style="left:700px; top:76px; height:30px;"></span>

  <section class="product-line line-paranuss">
    <div class="lid" style="top:30px;">
      <div class="lid-ring"><div class="lid-face">
        <div class="brand"><span class="brand-dot"></span>Kernhof</div>
        <div class="nut-visual" role="img" aria-label="Abbildung Paranüsse mit Blatt"></div>
        <div class="product-name">Paranuss</div>
        <span class="product-type">Mus</span>
      </div></div>
    </div>

    <div class="jar-label" style="top:382px;">
      <div class="jar-main">
        <div class="brand"><span class="brand-dot"></span>Kernhof</div>
        <div class="nut-visual" role="img" aria-label="Abbildung Paranüsse"></div>
        <span class="weight">250 g</span>
      </div>
      <div class="vertical-band"><div class="stack"><span class="product-name">Paranuss</span><span class="product-type">Mus</span></div></div>
    </div>

    <div class="oil-label" style="top:220px;">
      <div class="brand">Kernhof</div>
      <div class="oil-paper">
        <div class="oil-disc"><div class="nut-visual" role="img" aria-label="Abbildung Paranüsse mit Blatt"></div></div>
        <div class="product-name">Paranuss</div>
        <span class="product-type">Öl</span>
        <span class="weight">100 ml</span>
      </div>
    </div>

    <div class="bag" style="top:78px;">
      <div class="bag-window nut-visual" role="img" aria-label="Sichtfenster mit Paranusskernen"></div>
      <div class="vertical-band"><div class="stack"><span class="product-name">Paranuss</span><span class="product-type">Kerne</span></div></div>
      <div class="brand"><span class="brand-dot"></span>Kernhof</div>
      <span class="weight">500 g</span>
    </div>
  </section>

  <section class="product-line line-cashew">
    <div class="lid" style="top:588px;">
      <div class="lid-ring"><div class="lid-face">
        <div class="brand"><span class="brand-dot"></span>Kernhof</div>
        <div class="nut-visual" role="img" aria-label="Abbildung Cashewkerne mit Blatt"></div>
        <div class="product-name">Cashew</div>
        <span class="product-type">Mus</span>
      </div></div>
    </div>

    <div class="jar-label" style="top:940px;">
      <div class="jar-main">
        <div class="brand"><span class="brand-dot"></span>Kernhof</div>
        <div class="nut-visual" role="img" aria-label="Abbildung Cashewkerne mit Blatt"></div>
        <span class="weight">250 g</span>
      </div>
      <div class="vertical-band"><div class="stack"><span class="product-name">Cashew</span><span class="product-type">Mus</span></div></div>
    </div>

    <div class="oil-label" style="top:778px;">
      <div class="brand">Kernhof</div>
      <div class="oil-paper">
        <div class="oil-disc"><div class="nut-visual" role="img" aria-label="Abbildung Cashewkerne mit Blatt"></div></div>
        <div class="product-name">Cashew</div>
        <span class="product-type">Öl</span>
        <span class="weight">100 ml</span>
      </div>
    </div>

    <div class="bag" style="top:636px;">
      <div class="bag-window nut-visual" role="img" aria-label="Sichtfenster mit Cashewkernen"></div>
      <div class="vertical-band"><div class="stack"><span class="product-name">Cashew</span><span class="product-type">Kerne</span></div></div>
      <div class="brand"><span class="brand-dot"></span>Kernhof</div>
      <span class="weight">500 g</span>
    </div>
  </section>

</main>
</body>
</html>
```